Ranked amongst the Best Colleges and Programs

the size of the ad is Full Page, with bleed*
8”x 10.75" plus 0.25" bleed'
you have two choices for the tagline .. please chose what ever you think will allow you to make a better ad.
The instructions on the brief are in red
I am looking for a hight quality modern ad to place in local weekly publications that will stand out .
I would like a ad that people will look at and say i would like to see what this ad is all about.
I apprecate creative work.
the ad should not be very crowded and the text should be able to be read.
if you decide to use people in the ad .. (you don't have to ) then it should be a male dressed in white shirt in and sports jacket.. or if you would like you can use a vector and then use male or female people.
please leave one inch on the bottom for the footer

Target Market(s)

potential middle class students from 23-35 years of age

Industry/Entity Type

education

Requirements
Must have
• .the " 98% employment rate" should stand out in the ad.. but should not be the main part of the ad
Nice to have
• creative
Should not have
• Should not be a very busy or crowded ad.. i prefer pictures of men but should be .. in a business suit .. that looks professional- white shirt

```html
<!DOCTYPE html>
<html lang="en">
<head>
<meta charset="utf-8">
<title>NVU Masters of Accounting</title>
<link rel="stylesheet" href="https://fonts.googleapis.com/css2?family=Poppins:wght@400;700;800&family=Oswald:wght@500;600&family=Bebas+Neue&display=swap">
<style>
  :root {
    --navy: #062c48;
    --navy-deep: #04233b;
    --yellow: #fdb400;
    --orange: #f28c00;
    --orange-bright: #ff7a00;
    --white: #ffffff;
    --ink: #1c1c1c;
  }
  * { margin: 0; padding: 0; box-sizing: border-box; }
  html, body { width: 910px; height: 1200px; overflow: hidden; background: var(--white); }
  body { font-family: "Poppins", sans-serif; }
  .ad { position: relative; width: 910px; height: 1200px; overflow: hidden; background: var(--white); }
  .backdrop { position: absolute; inset: 0; }
  .portrait {
    position: absolute; left: 519px; top: 247px; width: 391px; height: 565px;
    background: linear-gradient(180deg, rgba(230,230,232,0.25) 0%, rgba(245,245,247,0.9) 45%, #e9e6e2 100%);
    border-radius: 180px 180px 0 0;
  }
  .headline {
    position: absolute; left: 38px; top: 48px;
    font-size: 66px; line-height: 72px; letter-spacing: -0.5px; text-transform: uppercase;
  }
  .headline .light { display: block; font-weight: 400; color: var(--white); }
  .headline .bold { display: block; font-weight: 800; color: var(--yellow); }
  .divider { position: absolute; left: 38px; top: 358px; width: 455px; height: 6px; }
  .program {
    position: absolute; left: 38px; top: 399px; width: 462px; height: 95px;
    display: flex; border-radius: 18px; overflow: hidden;
  }
  .program .school {
    width: 127px; background: var(--white); color: var(--ink);
    font-family: "Oswald", sans-serif; font-weight: 600; font-size: 56px;
    display: flex; align-items: center; justify-content: center;
  }
  .program .title {
    flex: 1; margin-left: 5px; background: var(--orange); border-radius: 0 18px 18px 0;
    color: var(--white); font-weight: 800; font-size: 34px; line-height: 36px;
    padding: 10px 0 0 18px; text-transform: uppercase;
  }
  .ranked {
    position: absolute; left: 38px; top: 604px;
    font-weight: 800; font-size: 35px; color: var(--ink); letter-spacing: -0.3px;
  }
  .badges { position: absolute; left: 41px; top: 659px; display: flex; gap: 11px; }
  .badge {
    width: 199px; height: 144px; background: var(--navy); border-radius: 4px; position: relative;
  }
  .badge::before {
    content: ""; position: absolute; left: 15px; right: 11px; top: 15px; height: 43px;
    background: var(--white); border-radius: 3px;
  }
  .badge::after {
    content: ""; position: absolute; left: 15px; right: 40px; top: 80px; height: 40px;
    background: rgba(255,255,255,0.18); border-radius: 3px;
  }
  .stat { position: absolute; left: 40px; top: 876px; width: 260px; }
  .stat .figure {
    font-family: "Bebas Neue", sans-serif; font-weight: 400; font-size: 162px; line-height: 136px;
    color: var(--orange-bright); letter-spacing: 0; white-space: nowrap;
  }
  .stat .label {
    font-weight: 800; font-size: 31px; line-height: 31px; color: var(--ink); text-transform: uppercase; margin-top: 6px;
  }
  .outcomes {
    position: absolute; left: 329px; top: 886px; width: 581px; height: 180px;
    background: var(--yellow); border-radius: 10px 0 0 10px;
    box-shadow: 0 8px 10px rgba(0,0,0,0.12);
    padding: 31px 20px 0 40px;
    font-size: 22px; line-height: 28.5px; color: var(--ink); font-weight: 400; white-space: nowrap;
  }
</style>
</head>
<body>
<main class="ad">
  <svg class="backdrop" width="910" height="1200" viewBox="0 0 910 1200" aria-hidden="true">
    <polygon points="0,0 910,0 910,812 576,812 416,553 0,553" fill="var(--navy)"/>
    <polygon points="0,562 408,562 420,584 0,584" fill="var(--orange)"/>
    <polygon points="582,825 910,825 910,843 594,843" fill="var(--orange)"/>
  </svg>

  <div class="portrait" role="img" aria-label="Smiling young man in a white shirt pointing toward the program title"></div>

  <h1 class="headline">
    <span class="light">A Small</span>
    <span class="bold">Investment Today</span>
    <span class="light">A Big Difference</span>
    <span class="bold">Tomorrow</span>
  </h1>

  <svg class="divider" width="455" height="6" viewBox="0 0 455 6" aria-hidden="true">
    <rect x="0" y="2" width="455" height="2" fill="var(--white)"/>
    <rect x="0" y="0" width="134" height="6" rx="3" fill="var(--white)"/>
  </svg>

  <div class="program">
    <div class="school">NVU</div>
    <div class="title">Masters of<br>Accounting</div>
  </div>

  <h2 class="ranked">RANKED AMONGST</h2>
  <div class="badges">
    <div class="badge" role="img" aria-label="Best colleges ranking badge"></div>
    <div class="badge" role="img" aria-label="Best masters in accounting ranking badge"></div>
  </div>

  <div class="stat">
    <div class="figure">98%</div>
    <div class="label">Employment<br>Rate</div>
  </div>

  <p class="outcomes">NVU graduates have gone on to work in<br>various high-quality jobs in top firms,<br>earning impressive six-figure salaries as<br>well as opening successful businesses.</p>
</main>
</body>
</html>
```